Business card for acupunctist in Melbourne. Specialises in Fertility, pre and post natal care, pain

I am looking for a business card which is going to catch people eyes. Two sided, one side in a muted colour (keeping it feminine) (pink or yellow???)maybe with a little simple logo or picture, the other side I was thinking white with 3 colours (pink grey and yellow... Had these in mind.
Info on the card
Maren Quillby Acupuncture

Dr Maren Quillby (TCM Acupuncture)
Acupuncture for balancing body and mind.
Verdant Osprey Clinic
14 Corran Lane, Eastwood 3071.
96274158
0438215074
Marentcm@quorvenmail.com

Some other little logo/ designs I have liked are as follows:
http://www.tessrolfeclinic.com/rates-and-insurance/
http://www.corabethwinslow.com/
http://www.zd-needlework.co.uk/

Target Market(s)

professional women, people in pain, active people, people seeking a healthy lifefstyle.

Industry/Entity Type

Business

Font styles to use
Serif
Sans Serif

Colors
eea4c8
fde08a
aaaaaa

Requirements
Must have
• Must be eye catching, but not too loud and busy. Subltle is good. Simple is also good. The logo could be something that represents growth and health and nurturing. Again not too elaborate, very simple.
Thankyou
Should not have
• Electric colours, crazy fonts, Pictures of yin and yang, candles, or bodies.

```html
<!DOCTYPE html>
<html lang="en">
<head>
<meta charset="utf-8">
<title>Maren Quillby Acupuncture – Business Card</title>
<link rel="stylesheet" href="https://fonts.googleapis.com/css2?family=Arimo:wght@400;700&display=swap">
<style>
  :root {
    --stage: #0f4552;
    --stage-edge: #0a2f39;
    --pink: #e8318c;
    --pink-light: #ef5fa2;
    --pink-soft: #f27ab2;
    --plum: #4a1a33;
    --paper: #ffffff;
    --grey: #6e6e6e;
    --green: #1f9a4a;
  }
  html, body {
    margin: 0;
    width: 1200px;
    height: 1000px;
    overflow: hidden;
  }
  body {
    position: relative;
    background: radial-gradient(ellipse at 50% 45%, var(--stage) 0%, var(--stage-edge) 100%);
    font-family: "Arimo", Arial, sans-serif;
  }
  .card {
    position: absolute;
    width: 560px;
    height: 320px;
    overflow: hidden;
    box-shadow: 0 14px 30px rgba(0,0,0,0.35);
  }
  .card-front {
    left: 110px;
    top: 110px;
    background: var(--pink);
  }
  .card-front .facets {
    position: absolute;
    inset: 0;
  }
  .front-identity {
    position: absolute;
    left: 0;
    right: 0;
    top: 130px;
    text-align: center;
    color: var(--paper);
    font-weight: 700;
  }
  .front-identity .name {
    font-size: 34px;
    letter-spacing: 0.5px;
    line-height: 1.1;
  }
  .front-identity .practice {
    font-size: 26px;
    line-height: 1.2;
  }
  .card-back {
    left: 540px;
    top: 570px;
    background: var(--paper);
  }
  .card-back .band {
    position: absolute;
    left: 0;
    top: 140px;
  }
  .back-details {
    position: absolute;
    right: 30px;
    top: 26px;
    text-align: right;
    font-weight: 700;
  }
  .back-details .doctor {
    color: var(--pink);
    font-size: 30px;
    margin: 0;
  }
  .back-details .title {
    color: var(--grey);
    font-size: 15px;
    margin: 2px 0 18px;
  }
  .back-details .line {
    color: var(--green);
    font-size: 14px;
    margin: 0 0 8px;
  }
  .back-details .contact {
    margin-top: 22px;
  }
</style>
</head>
<body>
  <section class="card card-front" aria-label="Card front">
    <svg class="facets" width="560" height="320" viewBox="0 0 560 320" aria-hidden="true">
      <polygon points="280,160 560,0 560,320" fill="var(--pink-light)"/>
      <polygon points="280,160 560,320 0,320" fill="var(--pink-soft)" opacity="0.45"/>
    </svg>
    <div class="front-identity">
      <div class="name">MAREN QUILLBY</div>
      <div class="practice">Acupuncture</div>
    </div>
  </section>

  <section class="card card-back" aria-label="Card back">
    <svg class="band" width="240" height="110" viewBox="0 0 240 110" aria-hidden="true">
      <polygon points="0,70 240,0 170,110 0,110" fill="var(--pink)"/>
    </svg>
    <div class="back-details">
      <p class="doctor">Dr Maren Quillby</p>
      <p class="title">(TCM Acupuncture)</p>
      <p class="line">Acupuncture for balancing body and mind.</p>
      <p class="line">Verdant Osprey Clinic.</p>
      <p class="line">14 Corran Lane, Eastwood 3071.</p>
      <div class="contact">
        <p class="line">96274158</p>
        <p class="line">0438215074</p>
        <p class="line">Marentcm@quorvenmail.com</p>
      </div>
    </div>
  </section>
</body>
</html>
```